Magazine advertisement for wedding proposal

SPECS
Page size: 221,0-290,0
File format:Certified PDF PrintSpec_7Q2 (CMYK).
supply with crop marks on sheet mirror format
boundlessly knitted

CONTENT
I am going to ask my wife to marry me (again). I have bought a 1/1 page in her favourite Glossy. I would like the advertisement to present a letter from a type machine covered with some polaroid pictures of her. Idea is to mimic a guy in love writing a letter and dreaming away at her pictures. I would like the whole look and feel to be professional and in style. As such colours etc. may be changed and altered to make it a great integrated piece. I have added multiple pohoto's. Not all have to be used. You can choose which and how much you find most appealing. I At least want Photo Mara 1 to be used and one of the pictures with us together in white (couple).

The letter should read the following text:

Once in your lifetime you meet someone who changes everything.
She is going to do her thing with or without you. That's why she is a queen.

But we are just better together, babe...☺
That's why I want you to love me, stay with me and marry me. Would you?

Marieke,

Wil je met me trouwen?

-xxx-

Dorian

Requirements
Must have
• Be creative! This is just my first thought, but if you have an idea which you think is better, please let me know.
• - light & warm colours which all have the same look and feel (I do not like too much accent and opposite colours)
• - text as a love letter or poem
• - usage of Photo Mara 1
• - usage of couple photo
• - usage of both photo's with kids
Should not have
• - too cliché props - one or two things like hearts and flowers is ok, but dont overdo it

```html
<!DOCTYPE html>
<html lang="en">
<head>
<meta charset="utf-8">
<title>Would you? – Proposal advertisement</title>
<link rel="stylesheet" href="https://fonts.googleapis.com/css2?family=Bodoni+Moda:wght@400&family=Lobster&display=swap">
<style>
  :root {
    --page-bg: #ffffff;
    --frame-line: #3a3a3a;
    --magenta: #ec2a7e;
    --magenta-soft: #f07bb0;
    --magenta-glow: #f6a9c9;
    --ink-white: #ffffff;
    --band-dark: #2b2a29;
    --rose-script: #ec85a6;
    --photo-warm: #d9b39a;
    --photo-sky: #b8c3c9;
  }
  * { margin: 0; padding: 0; box-sizing: border-box; }
  html, body { width: 938px; height: 1200px; overflow: hidden; background: var(--page-bg); }
  .sheet {
    position: relative; width: 938px; height: 1200px;
    border: 1px solid var(--frame-line); background: var(--page-bg);
  }
  .advert {
    position: absolute; left: 44px; top: 44px; width: 849px; height: 1112px;
    background: var(--magenta); outline: 1px solid #7a3a55; overflow: hidden;
  }
  .hero-photo {
    position: absolute; left: 0; top: 0; width: 849px; height: 887px;
    background:
      radial-gradient(ellipse 46% 52% at 50% 40%, var(--magenta-glow) 0%, var(--magenta-soft) 45%, rgba(236,42,126,0) 100%),
      linear-gradient(180deg, var(--magenta) 0%, #ef4a91 60%, #c86bb6 88%, var(--magenta) 100%);
  }
  .poem { position: absolute; inset: 0; color: var(--ink-white); text-align: center; }
  .poem .line {
    position: absolute; left: 0; width: 100%; line-height: 1; white-space: nowrap;
  }
  .serif { font-family: "Bodoni Moda", "Didot", serif; font-weight: 400; }
  .script { font-family: "Lobster", cursive; }
  .crown { position: absolute; left: 384px; top: 817px; width: 82px; height: 48px; }
  .footer-band {
    position: absolute; left: 0; top: 887px; width: 849px; height: 182px;
    background: var(--band-dark);
  }
  .footer-photo { position: absolute; top: 0; height: 182px; }
  .footer-photo.left {
    left: 0; width: 184px;
    background: linear-gradient(160deg, var(--photo-sky) 0%, var(--photo-warm) 55%, #9a8b6e 100%);
  }
  .footer-photo.right {
    left: 664px; width: 185px;
    background: linear-gradient(200deg, #8f8478 0%, var(--photo-warm) 50%, #6d9a86 100%);
  }
  .proposal {
    position: absolute; left: 184px; top: 0; width: 480px; height: 182px;
    text-align: center; color: var(--ink-white);
  }
  .proposal p { position: absolute; left: 0; width: 100%; line-height: 1; font-size: 24px; }
  .proposal .question { font-size: 46px; color: var(--rose-script); }
</style>
</head>
<body>
<div class="sheet">
  <section class="advert">
    <div class="hero-photo" role="img" aria-label="Portrait photo of the bride-to-be smiling, tinted in warm pink"></div>

    <div class="poem">
      <p class="line serif" style="top:63px;font-size:33px;">Once in your</p>
      <p class="line script" style="top:110px;font-size:76px;">lifetime</p>
      <p class="line serif" style="top:209px;font-size:31px;">you meet</p>
      <p class="line script" style="top:245px;font-size:76px;">someone</p>
      <p class="line serif" style="top:342px;font-size:31px;">who changes</p>
      <p class="line script" style="top:388px;font-size:84px;">everything.</p>
      <p class="line serif" style="top:490px;font-size:33px;">She is going to do</p>
      <p class="line serif" style="top:540px;font-size:33px;">her thing with or</p>
      <p class="line script" style="top:582px;font-size:80px;">without you.</p>
      <p class="line serif" style="top:687px;font-size:33px;">That's why she is a</p>
      <p class="line script" style="top:734px;font-size:76px;">Queen.</p>
      <svg class="crown" viewBox="0 0 82 48" aria-hidden="true">
        <path d="M6 16 L22 30 L41 8 L60 30 L76 16 L70 40 L12 40 Z" fill="none" stroke="#fff" stroke-width="4" stroke-linejoin="round"/>
        <rect x="12" y="40" width="58" height="6" fill="#fff"/>
        <circle cx="41" cy="5" r="4" fill="#fff"/>
        <circle cx="6" cy="13" r="3.5" fill="#fff"/>
        <circle cx="76" cy="13" r="3.5" fill="#fff"/>
      </svg>
    </div>

    <div class="footer-band">
      <div class="footer-photo left" role="img" aria-label="Photo of mother and daughter smiling outdoors"></div>
      <div class="proposal serif">
        <p style="top:14px;">But we are just better together, babe</p>
        <p style="top:48px;">That's why I want you to love me,</p>
        <p style="top:82px;">stay with me and marry me.</p>
        <p class="question script" style="top:114px;">Would you?</p>
      </div>
      <div class="footer-photo right" role="img" aria-label="Photo of mother and son laughing together"></div>
    </div>
  </section>
</div>
</body>
</html>
```